Summer Fun

I need a Poster for Front of hotel advertising discounted drinks on Thursday & Fridays
$3.50.
Schooners of Local Beer, Glass of House Wine & Bubbly.
From 3.30pm to 6.30 pm
Nibblies Provided

Target Market(s)

25 + Market

Industry/Entity Type

Hotel

Requirements
Should not have
• Do not want to be known as Happy Hour.

```html
<!DOCTYPE html>
<html lang="en">
<head>
<meta charset="utf-8">
<title>Thursday &amp; Friday $3.50 Drinks</title>
<link href="https://fonts.googleapis.com/css2?family=Oswald:wght@500;600&display=swap" rel="stylesheet">
<style>
  :root {
    --bg-deep: #0b0b0c;
    --bg-mid: #2a2a2c;
    --glow: #9a9a9c;
    --pink: #ec1c5f;
    --orange: #f7901e;
    --yellow: #f6e400;
    --lime: #b6d432;
    --amber: #b8862a;
    --ink-gradient: linear-gradient(90deg, var(--pink) 0%, var(--orange) 45%, var(--yellow) 78%, var(--lime) 100%);
  }
  html, body {
    margin: 0;
    padding: 0;
    overflow: hidden;
    background: var(--bg-deep);
  }
  .poster {
    position: relative;
    width: 846px;
    height: 1200px;
    overflow: hidden;
    background:
      radial-gradient(ellipse 420px 520px at 650px 380px, var(--glow) 0%, #5a5a5c 35%, var(--bg-mid) 65%, transparent 100%),
      linear-gradient(180deg, #1a1a1b 0%, var(--bg-deep) 100%);
    font-family: "Oswald", "Arial Narrow", sans-serif;
    font-weight: 600;
  }
  .drinks-photo {
    position: absolute;
    left: 414px;
    top: 87px;
    width: 378px;
    height: 1090px;
    border-radius: 40px;
    background:
      radial-gradient(ellipse 140px 80px at 60% 18%, rgba(160, 40, 40, 0.55), transparent 75%),
      radial-gradient(ellipse 170px 160px at 48% 55%, rgba(200, 150, 40, 0.55), transparent 75%),
      radial-gradient(ellipse 150px 90px at 50% 86%, rgba(150, 80, 20, 0.6), transparent 75%),
      radial-gradient(ellipse 190px 520px at 50% 50%, rgba(200, 200, 200, 0.18), transparent 80%);
  }
  .line {
    position: absolute;
    left: 51px;
    margin: 0;
    line-height: 1;
    white-space: nowrap;
    text-transform: uppercase;
    background: var(--ink-gradient);
    -webkit-background-clip: text;
    background-clip: text;
    color: transparent;
  }
  .days { font-size: 88px; letter-spacing: 0.5px; }
  .days--first { top: 49px; }
  .days--second { top: 145px; }
  .price { top: 260px; font-size: 158px; letter-spacing: -2px; }
  .hours { top: 467px; font-size: 40px; text-transform: none; }
  .offer { font-size: 58px; }
  .nibbles { top: 1104px; font-size: 47px; }
</style>
</head>
<body>
<main class="poster">
  <div class="drinks-photo" role="img" aria-label="Photo of a balanced stack of drinks: martini glass, red wine glass, beer mug and brandy snifter"></div>

  <h1 class="line days days--first">Thursday</h1>
  <h1 class="line days days--second">&amp; Friday</h1>
  <p class="line price">$3.50</p>
  <p class="line hours">3:30pm - 6:30pm</p>

  <p class="line offer" style="top:566px">Schooners</p>
  <p class="line offer" style="top:628px">of Local</p>
  <p class="line offer" style="top:690px">Beer</p>
  <p class="line offer" style="top:752px">Glass</p>
  <p class="line offer" style="top:814px">of House</p>
  <p class="line offer" style="top:876px">Wine</p>
  <p class="line offer" style="top:938px">&amp; Bubbly</p>

  <p class="line nibbles">Nibblies Provided</p>
</main>
</body>
</html>
```